Quarrytide
Quarrytide - Financial Services
Financial Services
www.quarrytidepay.com
Our team has been providing solutions for workers compensation for business owners for over 22 years, our service is provoided at no charge (as it is paid for by the vendor). What makes us unique is our ability to write just about every size company (3 man to 1000) and industry in every state,. Our programs simlyfy the business owners way of doing business by eliminationg several annoying functions that business owners face. For example, with our program a business owner would write one check for payroll, that check would cover his payroll, workers compensation, payroll taxes, employee deductions and garnishments, direct deposit and benefit deductions, year end W-2's and the liabilities that come with year end W-2's. Our program we keeps business owners compliant by keeping them informed about new requirements, labor laws, we provide all employee applications, safety posters, they are able to call with any employee related questions about hiring and firing and so on. All usually for less that they can do it themselves.
Busy, wordy
Service Oriented
White/possible grey, logo colors
Blues and whites and greys, logo colors
left side
We have a content writer completing the text, our home page will contain very little text and focus more as a landing page. The site itself needs to be very clean, simple and easy to navigate but will also allow viewers to go deep into the site if they want to find information, yet at the same time it will not force people away because of too much content

```html
<!DOCTYPE html>
<html lang="en">
<head>
<meta charset="utf-8">
<title>Quarrytide - Financial Services</title>
<link href="https://fonts.googleapis.com/css2?family=Arimo:wght@400;700&family=Tinos:wght@700&display=swap" rel="stylesheet">
<style>
  :root{
    --navy:#0d4f9e;
    --navy-dark:#083a78;
    --blue:#1d6fc4;
    --sky:#dbe9f5;
    --text:#4a4a4a;
    --muted:#7a7a7a;
    --line:#d9d9d9;
    --footer:#6d6d6d;
    --footer-dark:#555;
    --white:#fff;
  }
  *{margin:0;padding:0;box-sizing:border-box}
  html,body{width:1200px;height:845px;overflow:hidden;background:var(--white)}
  body{font-family:"Arimo",Arial,sans-serif;color:var(--text);position:relative}

  .top-band{position:absolute;left:0;top:90px;width:1200px;height:210px;
    background:linear-gradient(#e8f0f8,var(--sky) 60%,#eef3f8)}
  .lower-band{position:absolute;left:0;top:300px;width:1200px;height:140px;
    background:linear-gradient(#f1f3f5,#ffffff)}

  .brand{position:absolute;left:148px;top:16px;display:flex;align-items:center;gap:12px}
  .brand-dot{width:62px;height:62px;border-radius:50%;
    background:radial-gradient(circle at 40% 35%,#cfd8e2,#6f8296)}
  .brand-name{font-size:40px;font-weight:700;color:var(--navy);letter-spacing:.5px}

  .main-nav{position:absolute;left:497px;top:0;width:540px;height:50px;
    background:linear-gradient(#1a66bd,var(--navy-dark));border-radius:0 0 10px 10px;
    display:flex;align-items:center;padding-left:10px;gap:4px}
  .main-nav a{color:var(--white);text-decoration:none;font-size:17px;padding:0 16px;
    height:50px;line-height:50px}
  .main-nav a.active{background:linear-gradient(#9aa3ad,#6f7780)}

  .hero{position:absolute;left:149px;top:103px;width:900px;height:310px;
    border:5px solid var(--white);box-shadow:0 0 6px rgba(0,0,0,.25);
    background:linear-gradient(160deg,#ffffff 20%,#e3ecf5 55%,#6f9cd0 100%)}
  .hero-slogan{position:absolute;right:20px;top:200px;text-align:right;
    font-family:"Tinos",Georgia,serif;font-weight:700;color:var(--white);
    text-shadow:1px 1px 3px rgba(0,0,0,.6)}
  .hero-slogan .title{font-size:26px}
  .hero-slogan .call{font-size:24px;margin-top:14px}
  .hero-slogan .phone{font-size:32px}

  .welcome{position:absolute;left:151px;top:455px;width:630px}
  .welcome h1{font-size:29px;font-weight:400;color:#222;display:flex;align-items:center;gap:12px;
    padding-bottom:10px;border-bottom:1px solid var(--line);margin-bottom:8px}
  .welcome h1 .dot{width:30px;height:30px;border-radius:50%;
    background:radial-gradient(circle at 40% 35%,#cfd8e2,#6f8296)}
  .welcome h1 strong{color:var(--navy)}
  .welcome p{font-size:14.5px;line-height:21px;margin-bottom:22px}
  .welcome ul{list-style:none}
  .welcome li{font-size:14.5px;line-height:21px;padding-left:18px;position:relative}
  .welcome li::before{content:"";position:absolute;left:2px;top:7px;width:0;height:0;
    border-left:6px solid var(--blue);border-top:4px solid transparent;border-bottom:4px solid transparent}

  .news{position:absolute;left:847px;top:456px;width:202px}
  .news-head{height:36px;background:linear-gradient(#1f74cc,var(--navy));color:var(--white);
    font-size:21px;line-height:36px;padding-left:44px;position:relative}
  .news-head::before{content:"";position:absolute;left:10px;top:7px;width:24px;height:22px;
    background:var(--white);border-radius:2px}
  .news-item{border-bottom:1px solid var(--line);padding:12px 0 8px}
  .news-meta{display:flex;justify-content:space-between;font-size:11px}
  .news-meta b{color:var(--navy)}
  .news-meta span{color:var(--muted)}
  .news-item p{font-size:10.5px;line-height:13px;margin-top:6px}
  .news-more{text-align:right;font-size:11px;color:var(--navy);margin-top:10px}
  .news-more::before{content:"";display:inline-block;margin-right:5px;
    border-left:5px solid #3c9c3c;border-top:4px solid transparent;border-bottom:4px solid transparent}

  .site-footer{position:absolute;left:0;top:763px;width:1200px;height:82px;
    background:linear-gradient(var(--footer),var(--footer-dark))}
  .footer-links{position:absolute;left:151px;top:20px;font-size:13px;color:var(--white)}
  .footer-links span{margin:0 6px;color:#bbb}
  .copyright{position:absolute;left:151px;top:46px;font-size:12px;color:#ddd}
  .footer-brand{position:absolute;left:848px;top:12px;display:flex;align-items:center;gap:10px}
  .footer-brand .brand-dot{width:50px;height:50px}
  .footer-brand .brand-name{font-size:30px;color:var(--white)}
</style>
</head>
<body>
  <div class="top-band"></div>
  <div class="lower-band"></div>

  <header>
    <div class="brand"><div class="brand-dot"></div><div class="brand-name">QUARRYTIDE</div></div>
    <nav class="main-nav">
      <a class="active" href="#">HOME</a><a href="#">ABOUT US</a><a href="#">SERVICES</a><a href="#">HELP</a><a href="#">CONTACT US</a>
    </nav>
  </header>

  <section class="hero" role="img" aria-label="Photo of blue figures standing on a connected network of lines">
    <div class="hero-slogan">
      <div class="title">Solution Oriented</div>
      <div class="call">Call us at</div>
      <div class="phone">(555)-014-7720</div>
    </div>
  </section>

  <main class="welcome">
    <h1><span class="dot"></span>Welcome to <strong>QUARRYTIDE</strong></h1>
    <p>Maecenas vestibulum nibh sed lectus vulputate quis eleifend velit placerat. Phasellus dictum, mauris at dignissim tincidunt, erat quam mattis nisl, quis condimentum mauris orci non massa.</p>
    <p>Nunc neque felis, pellentesque sit amet congue eget, interdum at magna. Donec tincidunt rutrum diam eget fringilla. Pellentesque nec magna sit amet metus congue convallis.</p>
    <ul>
      <li>Curabitur iaculis metus vitae arcu vestibulum sagittis.</li>
      <li>Bras dapibus dapibus mauris, a porta odio placerat quis.</li>
      <li>Sed sed lorem id ipsum congue euismod.</li>
      <li>Htiam fringilla sem sit amet nulla lobortis hendrerit sit amet eu odio.</li>
    </ul>
  </main>

  <aside class="news">
    <div class="news-head">LATEST NEWS</div>
    <div class="news-item">
      <div class="news-meta"><b>Payroll Notes</b><span>21-Sep-2011</span></div>
      <p>Quarterly payroll updates and new compliance notes for owners across every state.</p>
      <div class="news-more">Read more</div>
    </div>
    <div class="news-item">
      <div class="news-meta"><b>Payroll Notes</b><span>21-Sep-2011</span></div>
      <p>Quarterly payroll updates and new compliance notes for owners across every state.</p>
      <div class="news-more">Read more</div>
    </div>
  </aside>

  <footer class="site-footer">
    <div class="footer-links">Home<span>|</span>About Us<span>|</span>Services<span>|</span>Help<span>|</span>Contact Us</div>
    <div class="copyright">Copyright (c) QUARRYTIDE. All rights reserved.</div>
    <div class="footer-brand"><div class="brand-dot"></div><div class="brand-name">QUARRYTIDE</div></div>
  </footer>
</body>
</html>
```